Framed Poster for my Home- song lyrics

Poster with song lyrics by the Varlow. The lyrics need to be printed onto paper- needs to be very high quality and then I want to have it framed

size 11x17

Show me Show Me Show Me How You Do That Trick...

Target Market(s)

Self

Font styles to use
Serif

Colors
85acd3
f68d4d
f37122

Requirements
Must have
• Great Font and needs to be a very High quality poster-- it will be framed
Nice to have
• Color-- and a design behind the lyrics

```html
<!DOCTYPE html>
<html lang="en">
<head>
<meta charset="utf-8">
<title>Show Me How You Do That Trick – Lyric Poster</title>
<link href="https://fonts.googleapis.com/css2?family=EB+Garamond:wght@500;700;800&display=swap" rel="stylesheet">
<style>
  :root {
    --backdrop: #e4e4e4;
    --paper-light: #fbf0c6;
    --paper-deep: #f3dea0;
    --blue: #85acd3;
    --orange: #f37122;
    --orange-soft: #f68d4d;
    --ink: #1c1c1c;
    --cream-text: #fbefc8;
  }
  * { margin: 0; padding: 0; box-sizing: border-box; }
  html, body {
    width: 1200px; height: 3000px; overflow: hidden;
    background: var(--backdrop);
  }
  .poster {
    position: absolute; left: 50px; top: 650px;
    width: 1100px; height: 1700px;
    background: radial-gradient(ellipse at 50% 45%, var(--paper-light) 0%, var(--paper-deep) 100%);
    font-family: "EB Garamond", Georgia, serif;
    font-variant-ligatures: none;
    font-feature-settings: "liga" 0, "dlig" 0, "calt" 0, "swsh" 0;
    overflow: hidden;
  }
  .frame-lines { position: absolute; inset: 0; }
  .lyric {
    position: absolute; left: 309px; width: 482px;
    font-size: 168px; line-height: 1; font-weight: 500;
    white-space: nowrap;
  }
  .lyric.blue { color: var(--blue); }
  .lyric.orange { color: var(--orange); }
  .lyric.right { text-align: right; }
  .tag {
    position: absolute; font-size: 80px; white-space: nowrap;
  }
  .tag-how {
    left: 313px; top: 1023px; width: 475px; height: 77px; line-height: 80px;
    background: var(--orange); color: var(--cream-text); text-align: center; font-weight: 700;
  }
  .tag-do {
    left: 313px; top: 1114px; width: 183px; height: 81px; line-height: 84px;
    background: var(--blue); color: var(--cream-text); text-align: center; font-weight: 700;
  }
  .tag-that {
    left: 500px; top: 1114px; width: 288px; height: 81px; line-height: 84px;
    color: var(--blue); text-align: right; font-weight: 500;
  }
  .lyric-trick {
    position: absolute; left: 309px; width: 482px; top: 1186px;
    font-size: 148px; line-height: 1; font-weight: 800; color: var(--orange);
    text-align: center; white-space: nowrap;
  }
  .art { position: absolute; border-radius: 10px; }
  .turntable-blue { background: rgba(133,172,211,0.22); }
  .turntable-orange { background: rgba(246,141,77,0.22); }
  .notes-column { background: linear-gradient(180deg, rgba(28,28,28,0.06), rgba(28,28,28,0.03)); }
  .microphone { background: rgba(28,28,28,0.55); border-radius: 50px 50px 12px 12px; }
  .fork { background: rgba(28,28,28,0.12); }
  .pick { background: rgba(28,28,28,0.08); border-radius: 40%; }
</style>
</head>
<body>
<main class="poster">
  <svg class="frame-lines" width="1100" height="1700" viewBox="0 0 1100 1700">
    <g fill="var(--ink)">
      <line x1="228" y1="33" x2="888" y2="33" stroke="var(--ink)" stroke-width="4"/>
      <circle cx="203" cy="33" r="5"/><circle cx="215" cy="33" r="5"/>
      <circle cx="901" cy="33" r="5"/><circle cx="913" cy="33" r="5"/>
      <line x1="357" y1="56" x2="724" y2="56" stroke="var(--ink)" stroke-width="4"/>
      <circle cx="333" cy="56" r="5"/><circle cx="345" cy="56" r="5"/>
      <circle cx="736" cy="56" r="5"/><circle cx="748" cy="56" r="5"/>
      <circle cx="50" cy="1000" r="4"/><circle cx="61" cy="1000" r="4"/>
      <circle cx="50" cy="1011" r="4"/><circle cx="61" cy="1011" r="4"/>
      <circle cx="1032" cy="1000" r="4"/><circle cx="1043" cy="1000" r="4"/>
      <circle cx="1032" cy="1011" r="4"/><circle cx="1043" cy="1011" r="4"/>
    </g>
    <g fill="none" stroke="var(--ink)" stroke-width="4">
      <polyline points="50,1022 50,1635 1043,1635 1043,1022"/>
      <polyline points="64,1022 64,1618 1029,1618 1029,1022"/>
    </g>
    <g>
      <circle cx="165" cy="62" r="9" fill="#e8323c"/>
      <circle cx="130" cy="160" r="5" fill="var(--orange)"/>
      <circle cx="35" cy="345" r="11" fill="#2aa9a0"/>
      <circle cx="170" cy="430" r="11" fill="var(--orange)"/>
      <circle cx="85" cy="590" r="10" fill="#f2c230"/>
      <circle cx="160" cy="700" r="4" fill="#2aa9a0"/>
      <circle cx="5" cy="840" r="8" fill="#e8323c"/>
      <circle cx="145" cy="920" r="11" fill="#e8323c"/>
      <circle cx="890" cy="160" r="5" fill="var(--orange)"/>
      <circle cx="880" cy="450" r="3" fill="#e8323c"/>
      <circle cx="875" cy="605" r="3" fill="#f2c230"/>
      <circle cx="940" cy="770" r="6" fill="#a9a9a9"/>
      <circle cx="895" cy="925" r="4" fill="#e8323c"/>
      <circle cx="1070" cy="945" r="12" fill="#2aa9a0"/>
    </g>
  </svg>

  <div class="art notes-column" style="left:0;top:40px;width:190px;height:920px" role="img" aria-label="Scattered music notes and treble clefs along the left edge"></div>
  <div class="art notes-column" style="left:940px;top:40px;width:160px;height:920px" role="img" aria-label="Scattered music notes and treble clefs along the right edge"></div>

  <div class="lyric blue" style="top:95px">SHOW</div>
  <div class="lyric blue" style="top:249px">ME</div>
  <div class="art turntable-blue" style="left:575px;top:251px;width:216px;height:158px" role="img" aria-label="Line drawing of a record turntable in blue"></div>

  <div class="lyric orange" style="top:385px">SHOW</div>
  <div class="art turntable-orange" style="left:318px;top:540px;width:216px;height:159px" role="img" aria-label="Line drawing of a record turntable in orange"></div>
  <div class="lyric orange right" style="top:540px">ME</div>

  <div class="lyric blue" style="top:695px">SHOW</div>
  <div class="lyric blue" style="top:839px">ME</div>
  <div class="art turntable-blue" style="left:575px;top:834px;width:201px;height:161px" role="img" aria-label="Line drawing of a record turntable in blue"></div>

  <div class="tag tag-how">HOW YOU</div>
  <div class="tag tag-do">DO</div>
  <div class="tag tag-that">THAT</div>
  <div class="lyric-trick">TRICK</div>

  <div class="art fork" style="left:87px;top:1355px;width:164px;height:164px" role="img" aria-label="Tuning fork drawing"></div>
  <div class="art fork" style="left:840px;top:1355px;width:168px;height:164px" role="img" aria-label="Tuning fork drawing"></div>
  <div class="art pick" style="left:375px;top:1394px;width:53px;height:62px" role="img" aria-label="Guitar pick drawing"></div>
  <div class="art pick" style="left:652px;top:1394px;width:56px;height:62px" role="img" aria-label="Guitar pick drawing"></div>
  <div class="art microphone" style="left:496px;top:1355px;width:112px;height:280px" role="img" aria-label="Vintage stand microphone drawing"></div>
</main>
</body>
</html>
```